Infographic comparing two personal financial success strategies

Need an infographic designed comparing typical financial planning advice to my proprietary wealth platform "The Brightward Path Method". My system is designed primarily for business owners, professionals and executives who aspire to a work-optional lifestyle. I would like designs that use my websites color palette (www.corvenmq.com) and include my logo. The final design should highlight the differences between the typical approach and the benefits of the "The Brightward Path Method".

Target Market(s)

Business owners, professionals (doctors, lawyers, accoutnants, and business executives

Industry/Entity Type

Financial Service

Font styles to use
Sans Serif

Colors
33a6d7
0455a3
cee9f5

```html
<!DOCTYPE html>
<html lang="en">
<head>
<meta charset="utf-8">
<title>The Brightward Path Method</title>
<link href="https://fonts.googleapis.com/css2?family=Libre+Caslon+Text:wght@400;700&family=Open+Sans:wght@400;600;700&display=swap" rel="stylesheet">
<style>
:root{
  --navy:#0b2a6e;
  --royal:#0455a3;
  --sky:#33a6d7;
  --ice:#cee9f5;
  --mist:#eef7fc;
  --steel:#a8c3ce;
  --slate:#8fb0bd;
  --ink:#2b3a4a;
  --white:#ffffff;
}
*{margin:0;padding:0;box-sizing:border-box}
html,body{width:1200px;height:2752px;overflow:hidden}
body{position:relative;background:var(--mist);font-family:"Open Sans",Arial,sans-serif;color:var(--ink)}
.header{position:absolute;left:0;top:0;width:1200px;height:450px;background:linear-gradient(180deg,#0a2f75 0%,#0455a3 60%,#1a5fae 100%)}
.title{position:absolute;left:55px;font-family:"Libre Caslon Text",Georgia,serif;color:var(--white);letter-spacing:2px;line-height:1;white-space:nowrap}
.title-small{top:48px;font-size:58px}
.title-large{top:116px;font-size:94px;letter-spacing:1px}
.badge{position:absolute;left:840px;top:64px;width:312px;height:312px;border-radius:50%;border:10px solid var(--white);background:var(--royal)}
.mascot{position:absolute;left:36px;top:236px;width:214px;height:544px;border-radius:100px 100px 30px 30px;background:linear-gradient(180deg,#d9c7a6 0%,#8e949c 30%,#6d737b 100%)}
.bubble{position:absolute;left:305px;top:250px;width:266px;height:160px;border-radius:50%;background:var(--white);display:flex;flex-direction:column;align-items:center;justify-content:center;gap:6px}
.brand-name{font-family:"Open Sans",Arial,sans-serif;font-weight:700;color:var(--royal);text-transform:uppercase;letter-spacing:.5px;white-space:nowrap}
.bubble .brand-name{font-size:16px}
.brand-dot{width:38px;height:38px;border-radius:50%;background:var(--royal)}
.white-band{position:absolute;left:0;top:450px;width:1200px;height:350px;background:var(--white)}
.versus-label{position:absolute;top:620px;font-size:19px;font-weight:700;color:var(--white);text-align:center;line-height:1.2;text-transform:uppercase}
.vs-left{left:285px;width:210px}
.vs-right{left:870px;width:230px}
.overlay{position:absolute;left:0;top:0}
.item{position:absolute;font-size:17.5px;line-height:1.35;color:var(--ink)}
.item h3{font-size:19px;font-weight:700;text-transform:uppercase;margin-bottom:6px}
.item .sub{font-size:16px;font-weight:700;text-transform:uppercase;margin:-2px 0 10px}
.left h3{color:var(--navy)}
.right h3{color:var(--sky)}
.left{left:55px;width:285px}
.right{left:661px;width:310px}
.ticks{list-style:none;margin-top:10px}
.ticks li{position:relative;padding-left:28px;margin-bottom:10px}
.ticks li::before{content:"";position:absolute;left:0;top:4px;width:16px;height:16px;border-radius:50%;border:2px solid var(--sky);background:radial-gradient(circle,var(--sky) 0 3px,transparent 4px)}
.ticks.nested{margin-left:28px}
.numbered{list-style:none;margin-top:14px}
.numbered li{margin-bottom:16px}
.plant{position:absolute;left:730px;top:2285px;width:300px;height:265px;border-radius:30px;background:linear-gradient(180deg,#6e9fb6 0%,#9fbfcd 100%)}
.footer-brand{position:absolute;left:569px;top:2560px;display:flex;align-items:center;gap:16px}
.footer-brand .brand-dot{width:72px;height:72px}
.footer-brand .brand-name{font-size:34px;color:var(--navy)}
.tagline{position:absolute;left:657px;top:2612px;font-size:24px;color:var(--royal)}
.footer-band{position:absolute;left:0;top:2722px;width:1200px;height:30px;background:var(--navy)}
</style>
</head>
<body>
<header class="header">
  <div class="title title-small">THE BRIGHTWARD</div>
  <div class="title title-large">PATH METHOD</div>
  <div class="badge" role="img" aria-label="Icon of caring hands holding a house, family and money bag"></div>
</header>

<section class="white-band"></section>

<svg class="overlay" width="1200" height="2752" viewBox="0 0 1200 2752" aria-hidden="true">
  <path d="M0 800 Q30 790 60 800 T120 800 T180 800 T240 800 T300 800 T360 800 T420 800 T480 800 T540 800 T600 800 T660 800 T720 800 T780 800 T840 800 T900 800 T960 800 T1020 800 T1080 800 T1140 800 T1200 800 V812 H0Z" fill="var(--white)"/>
  <polygon points="244,629 300,580 540,580 540,678 300,678" fill="var(--steel)"/>
  <polygon points="830,580 1080,580 1141,629 1080,678 830,678" fill="var(--steel)"/>
  <circle cx="591" cy="629" r="72" fill="var(--navy)" stroke="#d6e3ea" stroke-width="6"/>
  <circle cx="793" cy="629" r="72" fill="var(--sky)" stroke="#d6e3ea" stroke-width="6"/>
  <circle cx="692" cy="629" r="42" fill="var(--steel)" stroke="#d6e3ea" stroke-width="4"/>
  <text x="692" y="638" text-anchor="middle" font-family="Open Sans,Arial,sans-serif" font-size="24" font-weight="700" fill="var(--navy)">VS</text>
  <g fill="none" stroke="var(--white)" stroke-width="5">
    <rect x="562" y="598" width="50" height="60" rx="4"/>
    <line x1="572" y1="614" x2="600" y2="614"/><line x1="572" y1="628" x2="600" y2="628"/><line x1="572" y1="642" x2="590" y2="642"/>
    <circle cx="612" cy="652" r="10"/><line x1="619" y1="659" x2="628" y2="668"/>
    <circle cx="793" cy="629" r="34"/><circle cx="793" cy="629" r="16"/>
    <line x1="770" y1="606" x2="782" y2="618"/><line x1="816" y1="606" x2="804" y2="618"/><line x1="770" y1="652" x2="782" y2="640"/><line x1="816" y1="652" x2="804" y2="640"/>
  </g>

  <line x1="415" y1="820" x2="415" y2="2652" stroke="var(--navy)" stroke-width="2"/>
  <g fill="none" stroke="var(--navy)" stroke-width="4" stroke-dasharray="3 5">
    <path d="M400 936 H265"/><path d="M400 1141 H265"/><path d="M400 1367 H265"/><path d="M400 1639 H265"/>
    <path d="M400 1987 H265"/><path d="M400 2253 H265"/><path d="M400 2479 H265"/><path d="M400 2624 H265"/>
  </g>
  <g fill="none" stroke="var(--sky)" stroke-width="4" stroke-dasharray="3 5">
    <path d="M430 936 H523 V848 H630"/><path d="M430 1141 H523 V1055 H630"/>
    <path d="M430 1367 H523 V1328 H630"/><path d="M430 1639 H523 V1554 H630"/>
    <path d="M430 1987 H523 V1952 H630"/><path d="M430 2253 H523 V2112 H630"/>
  </g>
  <g fill="none" stroke="var(--navy)" stroke-width="4">
    <path d="M272 926 L258 936 L272 946"/><path d="M272 1131 L258 1141 L272 1151"/><path d="M272 1357 L258 1367 L272 1377"/><path d="M272 1629 L258 1639 L272 1649"/>
    <path d="M272 1977 L258 1987 L272 1997"/><path d="M272 2243 L258 2253 L272 2263"/><path d="M272 2469 L258 2479 L272 2489"/><path d="M272 2614 L258 2624 L272 2634"/>
  </g>
  <g fill="none" stroke="var(--sky)" stroke-width="4">
    <path d="M624 838 L638 848 L624 858"/><path d="M624 1045 L638 1055 L624 1065"/><path d="M624 1318 L638 1328 L624 1338"/>
    <path d="M624 1544 L638 1554 L624 1564"/><path d="M624 1942 L638 1952 L624 1962"/><path d="M624 2102 L638 2112 L624 2122"/>
  </g>
  <g font-family="Open Sans,Arial,sans-serif" font-size="19" font-weight="700" fill="var(--white)" text-anchor="middle">
    <circle cx="415" cy="936" r="18" fill="var(--navy)" stroke="var(--white)" stroke-width="3"/><text x="415" y="943">1</text>
    <circle cx="415" cy="1141" r="18" fill="var(--navy)" stroke="var(--white)" stroke-width="3"/><text x="415" y="1148">2</text>
    <circle cx="415" cy="1367" r="18" fill="var(--navy)" stroke="var(--white)" stroke-width="3"/><text x="415" y="1374">3</text>
    <circle cx="415" cy="1639" r="18" fill="var(--navy)" stroke="var(--white)" stroke-width="3"/><text x="415" y="1646">4</text>
    <circle cx="415" cy="1987" r="18" fill="var(--navy)" stroke="var(--white)" stroke-width="3"/><text x="415" y="1994">5</text>
    <circle cx="415" cy="2253" r="18" fill="var(--navy)" stroke="var(--white)" stroke-width="3"/><text x="415" y="2260">6</text>
    <circle cx="415" cy="2479" r="18" fill="var(--navy)" stroke="var(--white)" stroke-width="3"/><text x="415" y="2486">7</text>
    <circle cx="415" cy="2624" r="18" fill="var(--navy)" stroke="var(--white)" stroke-width="3"/><text x="415" y="2631">8</text>
  </g>

  <g fill="var(--slate)">
    <text x="1105" y="860" font-family="Open Sans,Arial,sans-serif" font-size="70" text-anchor="middle" fill="none" stroke="var(--slate)" stroke-width="3">$</text>
    <path d="M1015 870 h20 v40 h-20z" fill="var(--royal)"/>
    <path d="M1040 875 h60 q30 0 40 15 l-40 20 h-60z"/>
    <rect x="1030" y="1085" width="70" height="90" rx="12" fill="none" stroke="var(--royal)" stroke-width="8" transform="rotate(-35 1065 1130)"/>
    <text x="1068" y="1145" font-family="Open Sans,Arial,sans-serif" font-size="44" font-weight="700" text-anchor="middle" fill="var(--royal)" transform="rotate(-35 1068 1130)">$</text>
    <rect x="1030" y="1175" width="30" height="40" fill="var(--royal)"/>
    <circle cx="1085" cy="1352" r="32" fill="var(--royal)"/>
    <text x="1085" y="1366" font-family="Open Sans,Arial,sans-serif" font-size="36" font-weight="700" text-anchor="middle" fill="var(--white)">%</text>
    <path d="M1010 1400 h80 q20 0 30 -20 v30 q-10 20 -30 20 h-80z"/>
    <rect x="1125" y="1375" width="22" height="50" fill="var(--royal)"/>
    <rect x="1060" y="1660" width="70" height="45" fill="var(--royal)" transform="rotate(-15 1095 1682)"/>
    <rect x="1040" y="1690" width="60" height="50" rx="12"/>
    <rect x="1015" y="1720" width="30" height="40" fill="var(--royal)" transform="rotate(-30 1030 1740)"/>
    <path d="M1030 1960 L1090 1905 L1150 1960 Z" fill="var(--royal)"/>
    <rect x="1042" y="1958" width="96" height="60"/>
    <rect x="1078" y="1980" width="24" height="38" fill="var(--white)"/>
    <circle cx="1100" cy="2100" r="14" fill="var(--royal)"/><circle cx="1125" cy="2080" r="10" fill="var(--royal)"/><circle cx="1080" cy="2078" r="9"/>
    <path d="M1040 2135 h70 q20 0 30 -12 l0 20 q-10 14 -30 14 h-70z"/>
    <rect x="1020" y="2128" width="20" height="34" fill="var(--royal)"/>
  </g>
</svg>

<div class="mascot" role="img" aria-label="Cartoon illustration of a businessman in a grey suit giving a thumbs up"></div>
<div class="bubble"><span class="brand-dot"></span><span class="brand-name">Corven Wealth Partners</span></div>

<div class="versus-label vs-left">Typical Financial Advice</div>
<div class="versus-label vs-right">Brightward Path Method ™</div>

<div class="item left" style="top:925px"><h3>Make Income</h3><p>Job, Company, Real-Estate, Investments, etc.</p></div>
<div class="item left" style="top:1130px"><h3>Pay Taxes</h3><p>Reduces income</p><ul class="ticks"><li>RRSP</li></ul></div>
<div class="item left" style="top:1356px"><h3>Pay Interest</h3><div class="sub">( Mortgage, Car Loan,<br>Credit Cards, etc. )</div><p>Reduces income</p><ul class="ticks"><li>Pay off faster</li></ul></div>
<div class="item left" style="top:1628px;width:300px"><h3>Pay for Lifestyle</h3><div class="sub">( Food, Shelter, Vacations,<br>Recreation, Education, etc. )</div><p>Reduces income</p><ul class="ticks"><li>Cut back on spending</li></ul></div>
<div class="item left" style="top:1976px;width:330px"><h3>Hope For</h3><p>good returns on what you can save</p></div>
<div class="item left" style="top:2242px"><h3>Hope Nothing</h3><p>Bad happens</p><ul class="ticks"><li>Laid-off, no work, fired, company fails, etc.</li><li>Can’t work for health reason(s)</li></ul></div>
<div class="item left" style="top:2468px"><h3>Hope You Don’t</h3><p>live too long in retirement</p></div>
<div class="item left" style="top:2613px"><h3>Minimizes Future</h3><p>lifestyle and dreams</p></div>

<div class="item right" style="top:837px"><h3>Cash Flow</h3><p>Job, Company, Real-Estate, Investments, etc.</p></div>
<div class="item right" style="top:1044px"><h3>Cash Flow Maximization</h3><p>Get the most from your money now, don’t reduce lifestyle</p><ul class="ticks"><li>Reduce taxes – Flow-through, RRSPs &amp; TFSAs</li><li>Recapture Interest expense – Use Opportunity Cost</li></ul></div>
<div class="item right" style="top:1317px"><h3>Cash Flow Protection</h3><p>Protect &amp; Multiple the uses of your money</p><ul class="ticks"><li>Protect your income</li><li>Create guaranteed savings</li></ul></div>
<div class="item right" style="top:1543px"><h3>Cash Flow Expansion</h3><p>Multiple your income streams and increase cash flow now</p><ul class="ticks"><li>Regularly add new income streams</li></ul><ul class="ticks nested"><li>Dividend and interest paying investments</li></ul><ol class="numbered"><li>1. Direct &amp; In-direct Real-estate</li><li>2. Private Business ownership</li><li>3. Company Stocks</li><li>4. Private Lending</li></ol></div>
<div class="item right" style="top:1941px"><h3>Work Because</h3><p>you want to…not because you have to!</p></div>
<div class="item right" style="top:2101px"><h3>Bluesky Think</h3><p>your goals, dreams and life!</p></div>

<div class="plant" role="img" aria-label="Illustration of a hand holding a plant growing dollar coins"></div>
<div class="footer-brand"><span class="brand-dot"></span><span class="brand-name">Corven Wealth Partners</span></div>
<div class="tagline">Live life on your terms</div>
<div class="footer-band"></div>
</body>
</html>
```